ambitious event and festival agency from austria needs fresh business card design

A new design is due for the new headquarters and the new challenges. We organize events for different target groups from 16 to 60 years. The design should therefore be straightforward and not confused, so we are open to new colors and the logo may also be changed. In general, however, the most interesting suggestions are the most interesting ones. after this order we are looking for more graphics for partyvelt facebook instagramm homepage etc A new design is due for the new headquarters and the new challenges. We organize events for different target groups from 16 to 60 years. The design should therefore be straightforward and not confused, so we are open to new colors and the logo may also be changed. In general, however, the most interesting suggestions are the most interesting ones. after this order we are looking for more graphics for partyvelt facebook instagramm homepage etc A new design is due for the new headquarters and the new challenges. We organize events for different target groups from 16 to 60 years. The design should therefore be straightforward and not confused, so we are open to new colors and the logo may also be changed. In general, however, the most interesting suggestions are the most interesting ones. after this order we are looking for more graphics for partyvelt facebook instagramm homepage etc

Reason: I am sorry for this decision but i need some more time. No new designs please, there are so many good ones and I will have made a decision in the next 3 days.

Target Market(s)

Industry/Entity Type

Business

Font styles to use
Serif
Sans Serif

Colors

Designer to choose colors to be used in the design.

Requirements
Must have
Nice to have
Should not have

```html
<!DOCTYPE html>
<html lang="en">
<head>
<meta charset="utf-8">
<title>partyvelt business cards</title>
<link href="https://fonts.googleapis.com/css2?family=Montserrat:wght@600&family=Josefin+Sans:wght@300;600&family=Open+Sans:wght@400&display=swap" rel="stylesheet">
<style>
  :root {
    --paper: #ffffff;
    --backdrop-band: #dcdcdc;
    --card-light: #e4e4e4;
    --card-light-band: #c8c8c8;
    --charcoal: #333333;
    --charcoal-band: #393939;
    --red: #c8373b;
    --red-dark: #982a2f;
    --ink: #333333;
    --white: #ffffff;
  }
  * { margin: 0; padding: 0; box-sizing: border-box; }
  html, body { width: 1200px; height: 1200px; overflow: hidden; background: var(--paper); }
  .board { position: relative; width: 1200px; height: 1200px; }
  .backdrop { position: absolute; inset: 0; }
  .card { position: absolute; overflow: hidden; box-shadow: 6px 8px 10px rgba(0,0,0,0.35); }
  .card--front { left: 102px; top: 38px; width: 765px; height: 487px; background: var(--card-light); }
  .card--back { left: 353px; top: 556px; width: 770px; height: 488px; background: var(--charcoal); }
  .card__art { position: absolute; inset: 0; }
  .wordmark {
    position: absolute; font-family: "Montserrat", sans-serif; font-weight: 600;
    letter-spacing: -2px; line-height: 1; white-space: nowrap;
  }
  .card--front .wordmark { left: 40px; top: 22px; font-size: 96px; color: var(--white); }
  .card--back .wordmark { left: 40px; top: 120px; font-size: 96px; color: var(--white); }
  .details { position: absolute; left: 436px; top: 186px; font-family: "Josefin Sans", sans-serif; color: var(--ink); }
  .details__name { font-weight: 300; font-size: 30px; letter-spacing: 5px; line-height: 32px; }
  .details__role { font-weight: 600; font-size: 30px; letter-spacing: 6px; line-height: 32px; color: var(--red-dark); }
  .details__lines { margin-top: 22px; font-weight: 300; font-size: 18px; letter-spacing: 4px; line-height: 19px; }
  .contact { position: absolute; font-family: "Open Sans", sans-serif; font-size: 16px; line-height: 24px; }
  .card--front .contact { left: 436px; top: 366px; color: var(--ink); }
  .card--back .contact { right: 24px; top: 394px; color: var(--white); }
  .signature-mark {
    position: absolute; left: 716px; top: 1092px; font-family: "Montserrat", sans-serif;
    font-weight: 600; font-size: 86px; letter-spacing: -2px; line-height: 1; color: #111111;
  }
</style>
</head>
<body>
<main class="board">
  <svg class="backdrop" width="1200" height="1200" viewBox="0 0 1200 1200" aria-hidden="true">
    <polygon points="0,0 70,0 420,600 60,1200 0,1200" fill="var(--backdrop-band)"/>
    <polygon points="310,1010 520,1080 650,1110 500,1200 300,1200" fill="var(--card-light-band)"/>
  </svg>

  <section class="card card--front">
    <svg class="card__art" width="765" height="487" viewBox="0 0 765 487" aria-hidden="true">
      <polygon points="0,180 0,400 80,400 180,126 100,126" fill="var(--card-light-band)"/>
      <polygon points="150,400 260,400 380,126 270,126" fill="var(--card-light-band)"/>
      <polygon points="0,0 765,0 664,126 0,126" fill="var(--charcoal)"/>
      <rect x="0" y="453" width="765" height="34" fill="var(--red)"/>
      <polygon points="540,453 765,453 765,487 496,487" fill="var(--red-dark)"/>
    </svg>
    <div class="wordmark">partyvelt</div>
    <div class="details">
      <p class="details__name">LOREM IPSUM</p>
      <p class="details__role">LOREM IPSUM</p>
      <div class="details__lines">
        <p>LOREM IPSUM</p>
        <p>LOREM IPSUM</p>
        <p>LOREM IPSUM</p>
      </div>
    </div>
    <div class="contact">
      <p>www.partyvelt.eu</p>
      <p>office@partyvelt.eu</p>
    </div>
  </section>

  <section class="card card--back">
    <svg class="card__art" width="770" height="488" viewBox="0 0 770 488" aria-hidden="true">
      <polygon points="60,454 170,454 340,0 230,0" fill="var(--charcoal-band)"/>
      <polygon points="230,454 330,454 500,80 400,80" fill="var(--charcoal-band)"/>
      <rect x="0" y="454" width="770" height="34" fill="var(--red)"/>
      <polygon points="545,454 770,454 770,488 500,488" fill="var(--red-dark)"/>
    </svg>
    <div class="wordmark">partyvelt</div>
    <div class="contact">
      <p>www.partyvelt.eu</p>
      <p>office@partyvelt.eu</p>
    </div>
  </section>

  <div class="signature-mark">partyvelt</div>
</main>
</body>
</html>
```